Create custom funnel illustration

I've attached 3 files to this project. One is an example of the current design/colors so I'm looking for a design to match the current look & feel.

Second is a section of the website that we want to replace with the new infographic design.

Lastly, is a sample concept of what we're looking for.

Target Market(s)

40+ college educated

Industry/Entity Type

Business Software

Font styles to use
Sans Serif

Requirements
Must have
• Design to match the current look & feel. See "design-sample.png"

```html
<!DOCTYPE html>
<html lang="en">
<head>
<meta charset="utf-8">
<title>Modern Trust Funnel</title>
<link rel="stylesheet" href="https://fonts.googleapis.com/css2?family=Poppins:wght@400;700&display=swap">
<style>
  :root {
    --purple: #6a4fb0;
    --sky: #4eb0e6;
    --funnel: #cfcfcf;
    --rim: #eeeeee;
    --frame: #dcdcdc;
    --ink: #111111;
    --paper: #ffffff;
  }
  html, body {
    margin: 0;
    padding: 0;
    width: 1200px;
    height: 1200px;
    overflow: hidden;
    background: var(--paper);
  }
  .canvas {
    position: relative;
    width: 1200px;
    height: 1200px;
  }
  .infographic {
    position: absolute;
    left: 0;
    top: 0;
  }
  .panel-frame { fill: var(--paper); stroke: var(--frame); stroke-width: 1; }
  .funnel-body { fill: var(--funnel); }
  .funnel-rim { fill: var(--rim); }
  .funnel-mouth { fill: var(--funnel); }
  .connector { fill: none; stroke: var(--purple); stroke-width: 1.3; }
  .arrowhead { fill: var(--purple); }
  .icon-fill { fill: var(--purple); }
  .icon-accent { fill: var(--sky); }
  .icon-line { fill: none; stroke: var(--purple); stroke-width: 1.6; }
  .asset-label {
    font-family: "Poppins", sans-serif;
    font-size: 19px;
    fill: var(--ink);
    text-anchor: middle;
  }
  .asset-label .strong { font-weight: 700; }
  .trust-title {
    font-family: "Poppins", sans-serif;
    font-size: 29px;
    fill: var(--ink);
    text-anchor: middle;
  }
  .trust-title .strong { font-weight: 700; }
  .beneficiaries-label {
    font-family: "Poppins", sans-serif;
    font-size: 28px;
    fill: var(--ink);
    text-anchor: middle;
  }
  .beneficiaries-label .strong { font-weight: 700; }
</style>
</head>
<body>
<main class="canvas">
  <svg class="infographic" width="1200" height="1200" viewBox="0 0 1200 1200" xmlns="http://www.w3.org/2000/svg">
    <defs>
      <marker id="arrow" viewBox="0 0 10 10" refX="9" refY="5" markerWidth="6" markerHeight="6" orient="auto-start-reverse">
        <path class="arrowhead" d="M0,0 L10,5 L0,10 z"/>
      </marker>
    </defs>

    <rect class="panel-frame" x="69" y="347" width="1080" height="511"/>

    <!-- Funnel -->
    <g class="funnel">
      <path class="funnel-body" d="M373,506 L846,506 L661,684 Q652,693 652,705 L652,804 Q652,811 644,811 L600,811 Q570,800 567,780 L567,705 Q567,693 558,684 Z"/>
      <ellipse class="funnel-rim" cx="609" cy="503" rx="240" ry="19"/>
      <ellipse class="funnel-mouth" cx="611" cy="502" rx="233" ry="14"/>
    </g>

    <!-- Asset icons -->
    <g class="asset-icons">
      <g class="icon business-icon">
        <rect x="125" y="429" width="73" height="7" rx="2" class="icon-fill"/>
        <rect x="150" y="367" width="26" height="62" rx="6" class="icon-fill" role="img" aria-label="Business person standing with briefcase"/>
      </g>
      <g class="icon retirement-icon">
        <rect x="290" y="430" width="58" height="6" rx="2" class="icon-fill"/>
        <rect x="286" y="370" width="64" height="58" rx="14" class="icon-accent" role="img" aria-label="Person relaxing in a rocking chair"/>
      </g>
      <g class="icon stock-icon">
        <rect x="428" y="432" width="55" height="5" rx="1" class="icon-fill"/>
        <rect x="434" y="407" width="11" height="25" class="icon-fill"/>
        <rect x="450" y="399" width="11" height="33" class="icon-fill"/>
        <rect x="466" y="387" width="11" height="45" class="icon-fill"/>
        <path d="M435,401 Q455,395 465,381" class="icon-line" style="stroke: var(--sky)"/>
        <circle cx="448" cy="383" r="7" class="icon-accent"/>
      </g>
      <g class="icon bank-icon">
        <path d="M565,398 L607,376 L642,398 Z" class="icon-fill"/>
        <rect x="570" y="400" width="71" height="28" class="icon-fill"/>
        <rect x="581" y="404" width="8" height="20" fill="#fff"/>
        <rect x="599" y="404" width="8" height="20" fill="#fff"/>
        <rect x="617" y="404" width="8" height="20" fill="#fff"/>
        <rect x="567" y="429" width="75" height="5" class="icon-fill"/>
        <circle cx="604" cy="388" r="6" class="icon-accent"/>
      </g>
      <g class="icon property-icon">
        <path d="M757,390 L780,369 L803,390 L803,431 L757,431 Z" class="icon-line"/>
        <rect x="774" y="408" width="10" height="22" class="icon-fill"/>
        <rect x="773" y="385" width="14" height="12" class="icon-fill"/>
        <rect x="764" y="410" width="6" height="21" class="icon-accent"/>
        <rect x="757" y="430" width="46" height="5" class="icon-fill"/>
      </g>
      <g class="icon insurance-icon">
        <path d="M904,409 Q915,368 954,376 Q967,378 976,389 Q955,384 940,394 Q920,392 904,409 Z" class="icon-fill"/>
        <path d="M927,374 L944,428 Q944,433 939,432" fill="none" stroke="var(--sky)" stroke-width="2.5"/>
        <rect x="909" y="430" width="71" height="6" rx="2" class="icon-fill"/>
      </g>
      <g class="icon realestate-icon">
        <path d="M1035,402 L1072,377 L1108,402 Z" class="icon-fill"/>
        <rect x="1042" y="402" width="59" height="30" class="icon-fill"/>
        <rect x="1036" y="431" width="72" height="5" class="icon-fill"/>
        <path d="M1078,408 L1088,404 L1097,416 L1087,424 Z" class="icon-accent"/>
      </g>
    </g>

    <!-- Asset labels -->
    <g class="asset-labels">
      <text class="asset-label" x="163" y="458"><tspan class="strong">Business</tspan> interests</text>
      <text class="asset-label" x="316" y="458"><tspan class="strong">Retirement</tspan></text>
      <text class="asset-label" x="455" y="458"><tspan class="strong">Stock</tspan> market</text>
      <text class="asset-label" x="607" y="458"><tspan class="strong">Bank</tspan> accounts</text>
      <text class="asset-label" x="788" y="458"><tspan class="strong">Personal</tspan> property</text>
      <text class="asset-label" x="944" y="458"><tspan class="strong">Insurance</tspan></text>
      <text class="asset-label" x="1075" y="458"><tspan class="strong">Real estate</tspan></text>
    </g>

    <!-- Connectors -->
    <g class="connectors">
      <path class="connector" d="M138,477 H167 V609 H520" marker-end="url(#arrow)"/>
      <path class="connector" d="M307,477 H339 V584 H511" marker-end="url(#arrow)"/>
      <path class="connector" d="M438,477 H461 V554 H500" marker-end="url(#arrow)"/>
      <path class="connector" d="M631,477 H608 V541" marker-end="url(#arrow)"/>
      <path class="connector" d="M808,477 H785 V554 H719" marker-end="url(#arrow)"/>
      <path class="connector" d="M963,477 H931 V584 H706" marker-end="url(#arrow)"/>
      <path class="connector" d="M1099,477 H1070 V609 H699" marker-end="url(#arrow)"/>
    </g>

    <!-- Trust title -->
    <text class="trust-title">
      <tspan class="strong" x="607" y="584">Your</tspan>
      <tspan x="607" y="620">modern</tspan>
      <tspan x="607" y="654">Trust</tspan>
    </text>

    <!-- Beneficiaries -->
    <g class="beneficiaries" role="img" aria-label="Group of three trust beneficiaries">
      <rect x="579" y="746" width="18" height="65" rx="5" class="icon-accent"/>
      <rect x="600" y="746" width="19" height="65" rx="5" class="icon-fill"/>
      <rect x="622" y="746" width="18" height="65" rx="5" class="icon-accent"/>
    </g>
    <text class="beneficiaries-label" x="607" y="838">Trust <tspan class="strong">Beneficiaries</tspan></text>
  </svg>
</main>
</body>
</html>
```